Career development coaching - school lever to adults, needs a business card

Tandem Lark - An independent Career Advice business that provides 1-2-1 advice,for career development, entrepreneurial support and workshops needs a business card. Our clients of all ages (school leaver to adults looking for a career move) and universities and colleges. We would like the card to be double-sided with a modern, professional look. Looking for something professional yet very creative and original. Want a standard size business card that inspires a second look because it stands out from the rest.

One side of the card to have a design incorporating the logo with Tandem Lark name with the strap line “Helping you find your future” and space for the company website

Other side of the card to the logo/Tandem Lark name and the usual contact information:
Individual Name
Job Title (for example, Director)
Phone number
Email address
Company website address

Facebook, LinkedIn and Twitter links will need to go somewhere (back or front!)

The design will be used for 3 individuals so should be editable so that we can update as needed/as we grow.

Attached is the company logo/colours to be incorporated.

Target Market(s)

1-2-1 advice,for career development, entrepreneurial support and workshops needs a business card. Our clients of all ages (school leaver to adults looking for a career move) and universities and colleges.

Industry/Entity Type

Consulting

Contact Information for Business Card

Individual Name
Phone number
Email address
Company website address

Font styles to use
Sans Serif

Colors
0255a3
3176b5
faa54b
f78f20
85acd3
cfdeed

Requirements
Must have
• use the Tandem Lark Logo in some way - using the colours and the blue/orange palette
• For the logo - hope this makes sense to someone or if they direclty relate to the logo image attached!
• For the Orange:- Pantone 1585 C
• In CMYK : C3 M71 Y100 K0
• For the Blue:- 100% Pantone 7469 C
• In CMYK : C100 M62 Y27 K7
• Please feel free to contact me with any questions for more info
Nice to have
• happy to see any creative designs
Should not have
• Nothing too traditional,

```html
<!DOCTYPE html>
<html lang="en">
<head>
<meta charset="utf-8">
<title>Tandem Lark – Business Card</title>
<link rel="stylesheet" href="https://fonts.googleapis.com/css2?family=Roboto:wght@400;500;700&display=swap">
<style>
  :root {
    --blue-deep: #0b6f98;
    --blue: #1388b8;
    --blue-light: #1a9bcb;
    --orange: #f39a3c;
    --orange-deep: #f78f20;
    --white: #ffffff;
    --paper: #f4f4f4;
    --ink-muted: #2a5d86;
    --stage: #e9e6e1;
  }
  * { margin: 0; padding: 0; box-sizing: border-box; }
  html, body { width: 1200px; height: 1023px; overflow: hidden; }
  body {
    background: var(--stage);
    font-family: "Roboto", Arial, sans-serif;
    position: relative;
  }
  .card {
    position: absolute;
    left: 250px;
    width: 700px;
    height: 400px;
    border-radius: 22px;
    overflow: hidden;
    box-shadow: 0 6px 18px rgba(0,0,0,0.18);
  }
  .card--front { top: 72px; background: linear-gradient(135deg, var(--white), var(--paper)); }
  .card--back {
    top: 551px;
    background: radial-gradient(ellipse at 70% 60%, var(--blue-light), var(--blue-deep) 85%);
    color: var(--white);
  }
  .card__art { position: absolute; inset: 0; }

  .brand {
    position: absolute;
    display: flex;
    align-items: center;
    gap: 12px;
    font-weight: 500;
    letter-spacing: 1px;
    text-transform: uppercase;
    white-space: nowrap;
    z-index: 1;
  }
  .brand__dot { border-radius: 50%; flex: none; }
  .card--front .brand { left: 180px; top: 118px; color: var(--blue); font-size: 30px; }
  .card--front .brand__dot { width: 42px; height: 42px; background: var(--orange); }

  .person { position: absolute; left: 58px; top: 196px; }
  .person__name { color: var(--orange); font-size: 30px; font-weight: 500; }
  .person__role { color: var(--ink-muted); font-size: 15px; margin-top: 2px; }

  .contact { position: absolute; left: 58px; top: 268px; list-style: none; }
  .contact li {
    display: flex; align-items: center; gap: 10px;
    color: var(--ink-muted); font-size: 14px; line-height: 24px;
  }
  .contact svg { width: 14px; height: 14px; flex: none; }

  .social { position: absolute; right: 40px; top: 40px; list-style: none; text-align: right; }
  .social li {
    display: flex; align-items: center; justify-content: flex-end; gap: 8px;
    color: var(--white); font-size: 15px; line-height: 26px; letter-spacing: 0.5px;
  }
  .social__mark { width: 13px; height: 13px; background: var(--white); border-radius: 2px; }

  .card--back .brand { left: 0; right: 0; top: 110px; justify-content: center; font-size: 54px; color: var(--white); }
  .card--back .brand__dot { width: 60px; height: 60px; background: var(--white); }
  .tagline {
    position: absolute; left: 0; right: 0; top: 198px;
    text-align: center; font-size: 22px; letter-spacing: 1.5px;
  }
  .website {
    position: absolute; left: 0; right: 0; top: 290px;
    text-align: center; font-size: 15px; letter-spacing: 4px;
  }
  .website__domain { color: var(--orange); }
</style>
</head>
<body>

<section class="card card--front" aria-label="Card front">
  <svg class="card__art" viewBox="0 0 700 400" preserveAspectRatio="none" aria-hidden="true">
    <defs>
      <linearGradient id="waveBlue" x1="0" y1="0" x2="1" y2="1">
        <stop offset="0" stop-color="#1a9bcb"/>
        <stop offset="1" stop-color="#0b6f98"/>
      </linearGradient>
    </defs>
    <path d="M232,400 C330,372 400,330 440,280 C500,200 500,80 565,0 L700,0 L700,400 Z" fill="url(#waveBlue)"/>
    <path d="M222,400 C300,382 370,352 415,312 C385,362 320,388 270,400 Z" fill="#f39a3c"/>
  </svg>

  <div class="brand"><span class="brand__dot"></span>Tandem Lark</div>

  <div class="person">
    <p class="person__name">Your Name</p>
    <p class="person__role">Director</p>
  </div>

  <ul class="contact">
    <li>
      <svg viewBox="0 0 16 16"><path d="M4 1h3l1 4-2 1c1 2 2 3 4 4l1-2 4 1v3c0 1-1 2-2 2C7 14 2 9 2 3c0-1 1-2 2-2z" fill="none" stroke="#f39a3c" stroke-width="1.4"/></svg>
      01-234-56789
    </li>
    <li>
      <svg viewBox="0 0 16 16"><rect x="1.5" y="3.5" width="13" height="9" fill="none" stroke="#f39a3c" stroke-width="1.4"/><path d="M1.5 3.5 8 9l6.5-5.5" fill="none" stroke="#f39a3c" stroke-width="1.4"/></svg>
      hello@tandemlark.co
    </li>
    <li>
      <svg viewBox="0 0 16 16"><circle cx="8" cy="8" r="6.5" fill="none" stroke="#f39a3c" stroke-width="1.4"/><path d="M1.5 8h13M8 1.5c-3 3.5-3 9.5 0 13M8 1.5c3 3.5 3 9.5 0 13" fill="none" stroke="#f39a3c" stroke-width="1.2"/></svg>
      www.tandemlark.co
    </li>
  </ul>

  <ul class="social">
    <li>tandemlark <span class="social__mark"></span></li>
    <li>@tandemlark <span class="social__mark"></span></li>
  </ul>
</section>

<section class="card card--back" aria-label="Card back">
  <div class="brand"><span class="brand__dot"></span>Tandem Lark</div>
  <p class="tagline">Helping you find your future</p>
  <p class="website">www.<span class="website__domain">tandemlark</span>.co</p>
</section>

</body>
</html>
```